Brisk Hollow Builders Needs A Flyer

We need a flyer for our newest product "The Cedarlane Garden Workroom"

Here is some copy for the flyer:

1. More and more people everyday are working from home and finding it difficult to disconnect from home activities in order to focus on their work. They are also finding it very expensive to add on to their existing house for a quiet place. Our archatectually stunning, Cedarlane Garden Workroom is the answer. The office studio measures 16' wide and 10' deep. 160 Square feet of space.

Perfect for dozens of purposes. Home office, design studio, artist studio, home school office, reading room, craft studio, drafting room.

Features include:

- Steel Framing. 40-60% lighter then wood, higher strength to weight ratio, resistant to mold and fire and steel is the most recycled material on earth!
- Spray foam insulation. Cool in the summer and warm in the winter.
- HVAC Mini Split with wireless remote control and thermostat.
- 100% Off grid with enough solar and battery storage to run your entire office. No need to pay for an expensive electric installation.
- Flush fitting floor outlets to reduce wires.
- TV mount (Optional with pre-wired electric, HDMI, digital audio & Cat 6)
- Windows are tempered glass custom made by Morvik Glazing.
- Solar qualifies for a 26% tax credit. This is not a write-off rather it is a direct reduction on your tax obligation.
- Thousands of dollars less than adding onto your home.
- Custom color, siding, features available.

This beautiful back yard office is delivered 100% assembled and ready to enjoy on the day of delivery.

We ship nationwide from our factory in South Carolina. Give us a call anytime to speak to a designer and start your dream office today!

555-318-4027
info@BriskHollowBuilders.example

```html
<!DOCTYPE html>
<html lang="en">
<head>
<meta charset="utf-8">
<title>Brisk Hollow Builders – The Cedarlane Garden Workroom Flyer</title>
<link rel="stylesheet" href="https://fonts.googleapis.com/css2?family=Montserrat:ital,wght@0,400;0,500;0,600;0,700;0,800;1,400&family=Dancing+Script:wght@700&display=swap">
<style>
:root{
  --green:#62a84f;
  --green-dark:#2f7a32;
  --orange:#f3a81f;
  --ink:#333333;
  --footer-grey:#efefef;
  --white:#ffffff;
  --backdrop:#e4e4e2;
  --garden-light:#9fbf84;
  --garden-deep:#5f8a45;
  --wall-grey:#8a8c88;
  --interior-warm:#b9ada0;
  --line-grey:#ededed;
}
*{margin:0;padding:0;box-sizing:border-box}
html,body{width:1200px;height:768px;overflow:hidden;background:var(--backdrop)}
body{position:relative;font-family:"Montserrat",Arial,sans-serif;color:var(--ink)}
.page{position:absolute;top:36px;width:526px;height:676px;background:var(--white);overflow:hidden;box-shadow:0 2px 8px rgba(0,0,0,.18)}
.page--front{left:52px}
.page--back{left:626px}
.abs{position:absolute}

/* front */
.top-band{left:0;top:0;width:100%;height:52px;background:var(--green)}
.logo-box{left:25px;top:0;width:122px;height:94px;background:var(--white);border-bottom:3px solid var(--orange);display:flex;flex-direction:column;align-items:center;justify-content:center;gap:6px;z-index:3}
.logo-mark{width:14px;height:14px;border-radius:50%;background:var(--orange)}
.logo-name{font-weight:800;color:var(--green-dark);font-size:12px;line-height:1.15;text-align:center;text-transform:uppercase}
.site-url{right:23px;top:24px;color:var(--white);font-size:10px;font-weight:500}
.hero-photo{left:0;top:52px;width:100%;height:282px;background:linear-gradient(180deg,var(--garden-light),var(--garden-deep))}
.title-band{left:0;top:334px;width:100%;height:71px;background:var(--green)}
.title-front{left:30px;top:346px;font-weight:800;font-size:20px;line-height:23px;text-transform:uppercase}
.title-front .line-1{color:var(--orange);display:block}
.title-front .line-2{color:var(--white);display:block}
.render-photo{left:300px;top:343px;width:220px;height:142px;background:linear-gradient(180deg,#6b6e6b,var(--interior-warm))}
.intro{left:27px;top:421px;width:254px;font-size:8.4px;line-height:11.6px}
.measures{left:27px;top:509px;font-size:8.4px;line-height:14px;display:flex;gap:6px}
.measures ul{list-style:none}
.measures li::before{content:"";display:inline-block;width:3px;height:3px;background:var(--orange);margin-right:4px;vertical-align:middle}
.purpose-head{left:28px;top:546px;font-family:"Dancing Script",cursive;font-weight:700;color:var(--orange);font-size:18px}
.purpose-list{left:29px;top:574px;width:240px;font-style:italic;font-size:8.4px;line-height:12px}
.roof-photo{left:285px;top:499px;width:241px;height:99px;background:linear-gradient(180deg,var(--garden-deep),var(--wall-grey))}

/* footer */
.footer{left:0;top:617px;width:100%;height:59px;background:var(--footer-grey)}
.footer-text{left:27px;top:634px;width:310px;font-size:8.4px;font-weight:600;line-height:12px;color:#222}
.footer-contact{right:0;top:617px;width:196px;height:59px;background:var(--green);clip-path:polygon(16% 0,100% 0,100% 100%,0 100%);display:flex;flex-direction:column;align-items:flex-end;justify-content:center;padding-right:25px;color:var(--white)}
.phone{font-size:17px;font-weight:700;display:flex;align-items:center;gap:7px;line-height:1}
.email{font-size:8px;font-weight:500;display:flex;align-items:center;gap:4px;margin-top:4px}

/* back */
.features-head{left:30px;top:12px;color:var(--white);font-size:19px;font-weight:700}
.feature{display:flex;align-items:flex-start;gap:9px;font-size:8.4px;line-height:11.6px;position:absolute}
.feature .icon{flex:none;width:26px;height:26px;border-radius:50%;background:var(--orange);display:flex;align-items:center;justify-content:center;margin-top:-1px}
.feature .icon svg{width:14px;height:14px;stroke:var(--white);fill:none;stroke-width:1.4;stroke-linecap:round;stroke-linejoin:round}
.col-l{left:24px;width:252px}
.col-r{left:288px;width:230px}
.interior-photo{left:0;top:296px;width:290px;height:201px;background:linear-gradient(180deg,#7c7d79,var(--interior-warm))}
.frame-drawing{left:302px;top:298px;width:196px;height:102px;background:var(--line-grey)}
.soft-green{left:278px;top:416px;width:248px;height:20px;background:linear-gradient(180deg,rgba(98,168,79,0),rgba(98,168,79,.2))}
.delivery-box{left:297px;top:436px;width:229px;height:61px;background:var(--green);display:flex;align-items:center;gap:10px;padding-left:12px;color:var(--white);font-size:8.4px;line-height:12.4px}
.delivery-box::before{content:"";position:absolute;left:0;top:0;border-top:14px solid var(--orange);border-right:14px solid transparent}
.delivery-box svg{flex:none;width:30px;height:36px;stroke:var(--white);fill:none;stroke-width:2;stroke-linejoin:round;stroke-linecap:round}
.delivery-box strong{color:var(--orange);font-weight:700}
.title-back{left:32px;top:537px;font-weight:800;font-size:24px;line-height:27px;text-transform:uppercase}
.title-back .line-1{color:var(--orange);display:block}
.title-back .line-2{color:var(--green-dark);display:block}
.logo-back{left:352px;top:528px;width:140px;display:flex;flex-direction:column;align-items:center;gap:6px}
.logo-back .logo-mark{width:18px;height:18px}
.logo-back .logo-name{font-size:14px}
</style>
</head>
<body>

<section class="page page--front">
  <div class="abs top-band"></div>
  <div class="abs logo-box">
    <span class="logo-mark"></span>
    <span class="logo-name">Brisk Hollow<br>Builders</span>
  </div>
  <div class="abs site-url">www.BriskHollowBuilders.example</div>
  <div class="abs hero-photo" role="img" aria-label="Photo of the garden workroom with glass doors in a leafy back yard"></div>

  <div class="abs title-band"></div>
  <h1 class="abs title-front"><span class="line-1">The Cedarlane</span><span class="line-2">Garden Workroom</span></h1>
  <div class="abs render-photo" role="img" aria-label="Rendering of the workroom exterior with full-height windows"></div>

  <p class="abs intro">More and more people everyday are working from home and finding it difficult to disconnect from home activities in order to focus on their work. They are also finding it very expensive to add on to their existing house for a quiet place. Our archatectually stunning, Cedarlane Garden Workroom is the answer.</p>

  <div class="abs measures">
    <span>Measures :</span>
    <ul>
      <li>16' (wide) x 10' (deep)</li>
      <li>160 Square feet of space.</li>
    </ul>
  </div>

  <h2 class="abs purpose-head">Perfect for dozens of purposes.</h2>
  <p class="abs purpose-list">Home office, design studio, artist studio, home school office, reading room, craft studio, drafting room.</p>

  <div class="abs roof-photo" role="img" aria-label="Photo of the workroom roof fitted with solar panels"></div>

  <div class="abs footer"></div>
  <p class="abs footer-text">We ship nationwide from our factory in South Carolina. Give us a call anytime to speak to a designer and start your dream office today!</p>
  <div class="abs footer-contact">
    <div class="phone"><svg width="14" height="14" viewBox="0 0 24 24"><path fill="#fff" d="M6.6 10.8a15.1 15.1 0 0 0 6.6 6.6l2.2-2.2a1 1 0 0 1 1-.25 11.4 11.4 0 0 0 3.6.57 1 1 0 0 1 1 1V20a1 1 0 0 1-1 1A17 17 0 0 1 3 4a1 1 0 0 1 1-1h3.5a1 1 0 0 1 1 1c0 1.25.2 2.45.57 3.6a1 1 0 0 1-.25 1z"/></svg>555-318-4027</div>
    <div class="email"><svg width="8" height="6" viewBox="0 0 16 12"><rect width="16" height="12" fill="#fff"/><path d="M0 0l8 6 8-6" stroke="#62a84f" stroke-width="1.5" fill="none"/></svg>info@BriskHollowBuilders.example</div>
  </div>
</section>

<section class="page page--back">
  <div class="abs top-band"></div>
  <h2 class="abs features-head">Features</h2>

  <div class="feature col-l" style="top:72px"><span class="icon"><svg viewBox="0 0 16 16"><path d="M2 8l6-5 6 5M4 7v7h8V7"/><rect x="6.5" y="9" width="3" height="3"/></svg></span><p>Steel Framing. 40-60% lighter then wood, higher strength to weight ratio, resistant to mold and fire and steel is the most recycled material on earth!</p></div>
  <div class="feature col-l" style="top:124px"><span class="icon"><svg viewBox="0 0 16 16"><path d="M3 5q1.5 3 0 6M6 4q2 4 0 8M10 3v10l3-1V4z"/></svg></span><p>Spray foam insulation. Cool in the summer<br>and warm in the winter.</p></div>
  <div class="feature col-l" style="top:166px"><span class="icon"><svg viewBox="0 0 16 16"><path d="M7 2h2v8.5a2.5 2.5 0 1 1-2 0z"/></svg></span><p>HVAC Mini Split with wireless remote<br>control and thermostat.</p></div>
  <div class="feature col-l" style="top:206px"><span class="icon"><svg viewBox="0 0 16 16"><circle cx="8" cy="4" r="2"/><path d="M3 14l2-6h6l2 6zM4 11h8M8 8v6"/></svg></span><p>100% Off grid with enough solar and battery storage to run your entire office. No need to pay for an expensive electric installation.</p></div>
  <div class="feature col-l" style="top:259px"><span class="icon"><svg viewBox="0 0 16 16"><rect x="2.5" y="2.5" width="11" height="11" rx="1.5"/><circle cx="8" cy="8" r="3"/></svg></span><p style="margin-top:7px">Flush fitting floor outlets to reduce wires.</p></div>

  <div class="feature col-r" style="top:72px"><span class="icon"><svg viewBox="0 0 16 16"><rect x="2" y="3.5" width="12" height="8" rx="1"/><path d="M6 14h4"/></svg></span><p>TV mount (Optional with pre-wired<br>electric, HDMI, digital audio &amp; Cat 6)</p></div>
  <div class="feature col-r" style="top:114px"><span class="icon"><svg viewBox="0 0 16 16"><rect x="3.5" y="2" width="9" height="12"/><path d="M8 2v12M3.5 8h9"/></svg></span><p>Windows are tempered glass custom<br>made by Morvik Glazing.</p></div>
  <div class="feature col-r" style="top:155px"><span class="icon"><svg viewBox="0 0 16 16"><path d="M6 3h4l-1 2q4 2 4 6a2 2 0 0 1-2 2H5a2 2 0 0 1-2-2q0-4 4-6z"/><path d="M8 7v4"/></svg></span><p>Solar qualifies for a 26% tax credit. This is<br>not a write-off rather it is a direct reduction<br>on your tax obligation.</p></div>
  <div class="feature col-r" style="top:207px"><span class="icon"><svg viewBox="0 0 16 16"><circle cx="9" cy="5.5" r="3.5"/><path d="M2 12h3l3 1.5 5-2.5M9 4v3"/></svg></span><p>Thousands of dollars less than adding<br>onto your home.</p></div>
  <div class="feature col-r" style="top:253px"><span class="icon"><svg viewBox="0 0 16 16"><path d="M2 8l6-5 6 5M4 7v7h8V7M6 12l4-4"/></svg></span><p style="margin-top:7px">Custom color, siding, features available.</p></div>

  <div class="abs interior-photo" role="img" aria-label="Close-up photo of the workroom front with glass doors and furnished interior"></div>
  <div class="abs frame-drawing" role="img" aria-label="Technical drawing of the steel frame panels"></div>
  <div class="abs soft-green"></div>
  <div class="abs delivery-box">
    <svg viewBox="0 0 30 36"><path d="M5 14L15 5l10 9M8 12v9h14v-9"/><rect x="12.5" y="15" width="5" height="6"/><path d="M2 28h8l6 3 10-5"/></svg>
    <p>This beautiful back yard office is<br><strong>delivered 100% assembled</strong> and ready<br>to enjoy on the day of delivery.</p>
  </div>

  <h1 class="abs title-back"><span class="line-1">The Cedarlane</span><span class="line-2">Garden Workroom</span></h1>
  <div class="abs logo-back">
    <span class="logo-mark"></span>
    <span class="logo-name">Brisk Hollow<br>Builders</span>
  </div>

  <div class="abs footer"></div>
  <p class="abs footer-text">We ship nationwide from our factory in South Carolina. Give us a call anytime to speak to a designer and start your dream office today!</p>
  <div class="abs footer-contact">
    <div class="phone"><svg width="14" height="14" viewBox="0 0 24 24"><path fill="#fff" d="M6.6 10.8a15.1 15.1 0 0 0 6.6 6.6l2.2-2.2a1 1 0 0 1 1-.25 11.4 11.4 0 0 0 3.6.57 1 1 0 0 1 1 1V20a1 1 0 0 1-1 1A17 17 0 0 1 3 4a1 1 0 0 1 1-1h3.5a1 1 0 0 1 1 1c0 1.25.2 2.45.57 3.6a1 1 0 0 1-.25 1z"/></svg>555-318-4027</div>
    <div class="email"><svg width="8" height="6" viewBox="0 0 16 12"><rect width="16" height="12" fill="#fff"/><path d="M0 0l8 6 8-6" stroke="#62a84f" stroke-width="1.5" fill="none"/></svg>info@BriskHollowBuilders.example</div>
  </div>
</section>

</body>
</html>
```